Digital multi-page Product Brochure

We’re creating a product brochure for our Wood Look Porcelain Pavers. The brochure will show technical details of the pavers, available colors, and applications while also showcasing the advantages of porcelain over wood.
We prefer a clean design aesthetic with appropriate white space incorporated. Because we want the view to appreciate the detail and natural look of the porcelain pavers, we want relatively large color swatches in the available colors section.
Each color swatch section needs the information provided in the guide. The design and layout of these sections is completely open. We do want to see a visual of the paver size in each color swatch section along with the written sizing information.
Mixed use of renderings and actual installation photos. Style and placement of photos is up to designer.
Target Market(s)
Architects and contractors
Industry/Entity Type
Building Materials
Font styles to use
Other font styles liked:
- Outfit - headers, Helvetica for paragraph copy

```html
<!DOCTYPE html>
<html lang="en">
<head>
<meta charset="utf-8">
<title>Wood-Look Porcelain Pavers Brochure</title>
<link href="https://fonts.googleapis.com/css2?family=Outfit:wght@500;600;700&family=Arimo:wght@400;700&display=swap" rel="stylesheet">
<style>
:root{
  --ink:#1f3f4a;
  --teal:#146b73;
  --text:#2b2b2b;
  --bg:#e4e4e4;
  --paper:#ffffff;
  --rule:#ffffff;
}
*{box-sizing:border-box;margin:0;padding:0}
html,body{width:1200px;height:1024px;overflow:hidden;background:var(--bg)}
body{position:relative;font-family:Arimo,Helvetica,Arial,sans-serif;color:var(--text)}
.page{position:absolute;width:360px;height:466px;background:var(--paper);overflow:hidden;box-shadow:0 1px 3px rgba(0,0,0,.12)}
.p1{left:36px;top:35px}.p2{left:420px;top:35px}.p3{left:803px;top:35px}
.p4{left:36px;top:523px}.p5{left:420px;top:523px}
.photo{position:absolute}
.h-outfit{font-family:Outfit,sans-serif}
/* cover */
.cover-frame{position:absolute;left:14px;top:13px;width:332px;height:440px;border:1.5px solid var(--ink);z-index:1}
.cover-photo{left:0;top:183px;width:360px;height:283px;background:linear-gradient(180deg,#8a5a4a 0%,#a88a6e 30%,#8c8a78 55%,#c9c4bb 75%,#6f6b68 100%);z-index:2}
.cover-frame-lower{position:absolute;left:14px;top:183px;width:332px;height:270px;border:1px solid var(--rule);border-top:none;z-index:3}
.brand{position:absolute;left:30px;top:30px;display:flex;align-items:center;gap:5px;font-family:Outfit,sans-serif;font-weight:500;font-size:16px;color:var(--ink);z-index:4}
.brand i{display:block;width:10px;height:10px;background:var(--ink)}
.cover-title{position:absolute;left:30px;top:58px;font-family:Outfit,sans-serif;font-weight:600;font-size:15px;line-height:17px;color:var(--ink);padding-bottom:4px;border-bottom:1.5px solid var(--ink);z-index:4}
.checklist{position:absolute;left:31px;top:102px;list-style:none;z-index:4}
.checklist li{display:flex;align-items:center;gap:9px;font-size:7px;height:14px;color:var(--text)}
.checklist svg{width:7px;height:7px}
/* fire page */
.fire-photo{left:0;top:0;width:360px;height:466px;background:linear-gradient(180deg,#7b5244 0%,#8b6d5a 40%,#6a6a58 60%,#b7b2aa 80%,#8f8a84 100%)}
.fire-box{position:absolute;left:31px;top:16px;width:299px;height:123px;background:var(--ink);outline:1px solid var(--rule);outline-offset:-4px;border:1px solid var(--rule);text-align:center;padding:26px 22px 0}
.fire-box p{font-size:7px;line-height:11px;color:#fff}
.fire-box h3{font-family:Arimo,sans-serif;font-weight:700;font-size:12px;line-height:14px;color:#fff;margin-top:9px}
/* header band */
.band{position:absolute;left:0;top:0;width:360px;height:57px;background:var(--ink);display:flex;align-items:center;justify-content:center;font-family:Outfit,sans-serif;font-weight:600;font-size:17px;color:#fff}
.strip-photo{left:0;top:57px;width:360px;height:77px;background:linear-gradient(180deg,#8c5a48 0%,#9a7a62 40%,#7a8b5a 65%,#bdb8b0 100%)}
.intro{position:absolute;left:28px;top:145px;width:304px;text-align:center;font-size:6.6px;line-height:11px}
.vs-title{position:absolute;left:0;top:184px;width:360px;text-align:center;font-family:Outfit,sans-serif;font-weight:600;font-size:13px;color:var(--teal)}
.compare{position:absolute;left:35px;top:212px;width:297px;border-collapse:collapse;font-size:5.2px}
.compare th{height:18px;color:#fff;font-weight:700;text-align:center}
.compare th.c1{background:var(--ink)}.compare th.c2{background:var(--teal)}
.compare th.blank{background:transparent}
.compare td{height:21px}
.compare td.label{width:115px;background:var(--ink);color:#fff;font-weight:700;padding-left:12px;border-bottom:1px solid #3b5a63}
.compare td.mark{width:91px;text-align:center;font-size:6px;border-right:1px solid var(--ink)}
.compare tr:last-child td.mark{border-bottom:1px solid var(--ink)}
.compare td.mark.last{border-right:1px solid var(--ink)}
/* dimensions */
.strip-photo.tall{height:101px;background:linear-gradient(180deg,#8c5a48 0%,#9a7a62 45%,#7a8b5a 70%,#bdb8b0 100%)}
.sec-title{position:absolute;font-family:Outfit,sans-serif;font-weight:600;color:var(--teal)}
.sizes{position:absolute;left:27px;top:199px;font-weight:700;font-size:8.5px;line-height:14px;color:#222}
.label-sm{position:absolute;font-family:Outfit,sans-serif;font-weight:600;font-size:8.5px;color:var(--teal)}
.swatch{position:absolute}
.cap{position:absolute;font-size:5px;color:#444}
.variation-copy{position:absolute;left:27px;top:340px;width:145px;font-size:7px;line-height:11.3px;text-align:justify}
.var-key{position:absolute;left:27px;top:400px;font-weight:700;font-size:7px;line-height:11.5px}
.key-title{position:absolute;left:194px;top:382px;font-weight:700;font-size:7px}
.key{position:absolute;top:398px;font-size:5px}
.key svg{display:block;margin-top:2px;width:23px;height:23px}
/* styles */
.styles-sub{position:absolute;left:0;top:87px;width:360px;text-align:center;font-family:Outfit,sans-serif;font-weight:600;font-size:6.6px;color:#222}
.style-photo{position:absolute;width:143px;height:105px}
.style-name{position:absolute;font-family:Arimo,sans-serif;font-size:13px;color:#222}
.style-desc{position:absolute;font-size:6.8px;line-height:10px;color:#333}
</style>
</head>
<body>

<!-- Cover -->
<section class="page p1">
  <div class="cover-frame"></div>
  <div class="brand"><i></i>Timberlane</div>
  <h1 class="cover-title">EVERYTHING YOU NEED TO KNOW ABOUT<br>WOOD-LOOK&nbsp; PORCELAIN PAVERS</h1>
  <ul class="checklist">
    <li><svg viewBox="0 0 10 10"><path d="M1 5.5l3 3 5-7" fill="none" stroke="#146b73" stroke-width="2"/></svg>Advantages over Wood</li>
    <li><svg viewBox="0 0 10 10"><path d="M1 5.5l3 3 5-7" fill="none" stroke="#146b73" stroke-width="2"/></svg>Colors and Styles</li>
    <li><svg viewBox="0 0 10 10"><path d="M1 5.5l3 3 5-7" fill="none" stroke="#146b73" stroke-width="2"/></svg>Paver Sizes and Dimensions</li>
    <li><svg viewBox="0 0 10 10"><path d="M1 5.5l3 3 5-7" fill="none" stroke="#146b73" stroke-width="2"/></svg>Installation and Laying Options</li>
    <li><svg viewBox="0 0 10 10"><path d="M1 5.5l3 3 5-7" fill="none" stroke="#146b73" stroke-width="2"/></svg>Project Inspiration</li>
  </ul>
  <div class="photo cover-photo" role="img" aria-label="Rooftop terrace with lounge seating and a fountain on wood-look porcelain pavers between brick buildings"></div>
  <div class="cover-frame-lower"></div>
</section>

<!-- Fire rating -->
<section class="page p2">
  <div class="photo fire-photo" role="img" aria-label="Courtyard with a black steel fire pit and rocking chairs on porcelain pavers"></div>
  <div class="fire-box">
    <p>Wood look porcelain pavers used with our Emberline Steel Pedestals combine to create a 100% Fireproof decking installation. Fire codes and city requirements are frequently changing.</p>
    <h3>Our elevated decking system is<br>Class A fire rated.</h3>
  </div>
</section>

<!-- Porcelain advantage -->
<section class="page p3">
  <div class="band">THE PORCELAIN ADVANTAGE</div>
  <div class="photo strip-photo" role="img" aria-label="Rooftop terrace seating area with planters"></div>
  <p class="intro">Timberlane Wood-Look Porcelain Pavers and Planks beautifully incorporate all the features that make natural wood so appealing, while eliminating the challenges and drawbacks of using wood or composite wood for various projects and installations.</p>
  <h2 class="vs-title">WOOD-LOOK PORCELAIN PAVERS VS. WOOD</h2>
  <table class="compare">
    <tr><th class="blank"></th><th class="c1">WOOD-LOOK PAVERS</th><th class="c2">WOOD</th></tr>
    <tr><td class="label">Stays cool in the sun</td><td class="mark">x</td><td class="mark last"></td></tr>
    <tr><td class="label">100% water resistant</td><td class="mark">x</td><td class="mark last"></td></tr>
    <tr><td class="label">Scratch resistant</td><td class="mark">x</td><td class="mark last"></td></tr>
    <tr><td class="label">Fireproof</td><td class="mark">x</td><td class="mark last"></td></tr>
    <tr><td class="label">Low Maintenance</td><td class="mark">x</td><td class="mark last"></td></tr>
    <tr><td class="label">Fade resistant</td><td class="mark">x</td><td class="mark last"></td></tr>
    <tr><td class="label">Cold resistant (won’t warp or twist)</td><td class="mark">x</td><td class="mark last"></td></tr>
    <tr><td class="label">On-grade or pedestal supported</td><td class="mark">x</td><td class="mark last"></td></tr>
    <tr><td class="label">Slip resistant</td><td class="mark">x</td><td class="mark last"></td></tr>
    <tr><td class="label">Insect resistant</td><td class="mark">x</td><td class="mark last"></td></tr>
  </table>
</section>

<!-- Dimensions -->
<section class="page p4">
  <div class="band">DIMENSIONS AND FEATURES</div>
  <div class="photo strip-photo tall" role="img" aria-label="Rooftop terrace with brick buildings behind"></div>
  <h2 class="sec-title" style="left:0;top:169px;width:360px;text-align:center;font-size:13px">DIMENSIONS</h2>
  <p class="sizes">Slabs 24” x 48”, 24” x 24”<br>Planks 16” x 48”, 12” x 48”, 8” x 48”</p>
  <div class="label-sm" style="left:27px;top:238px">SLABS</div>
  <div class="label-sm" style="left:193px;top:238px">PLANKS</div>
  <div class="swatch" role="img" aria-label="Light oak wood-look slab swatch" style="left:28px;top:258px;width:44px;height:41px;background:linear-gradient(90deg,#b59a84,#c7b09c,#a98e78)"></div>
  <div class="cap" style="left:29px;top:302px">24” X 24”</div>
  <div class="swatch" role="img" aria-label="Grey wood-look slab swatch" style="left:82px;top:258px;width:67px;height:41px;background:linear-gradient(90deg,#bbb8b3,#cfccc7,#b4b1ab)"></div>
  <div class="cap" style="left:82px;top:302px">24” X 48”</div>
  <div class="swatch" role="img" aria-label="Weathered grey-brown plank swatch" style="left:193px;top:258px;width:137px;height:21px;background:linear-gradient(90deg,#6e6a62,#8a8378,#6f685e)"></div>
  <div class="cap" style="left:193px;top:282px">8” X 48”</div>
  <div class="swatch" role="img" aria-label="Rich brown plank swatch" style="left:193px;top:297px;width:137px;height:21px;background:linear-gradient(90deg,#8a5a44,#9c6a50,#85563f)"></div>
  <div class="cap" style="left:193px;top:322px">12” X 48”</div>
  <div class="swatch" role="img" aria-label="Natural taupe plank swatch" style="left:193px;top:334px;width:137px;height:21px;background:linear-gradient(90deg,#84715c,#97826a,#7c6a56)"></div>
  <div class="cap" style="left:193px;top:359px">16” X 48”</div>
  <h2 class="sec-title" style="left:27px;top:322px;font-size:12px;color:var(--ink)">VARIATION</h2>
  <p class="variation-copy">Slight tone variations are inherent in porcelain pavers, slabs, and planks. Some colors and styles have minimal variations between each paver and others are significantly distinct from one another.</p>
  <p class="var-key">V2 – minimal variation<br>V3 – moderate variation<br>V4 – significant variation</p>
  <div class="key-title">Examples for key</div>
  <div class="key" style="left:196px">V2
    <svg viewBox="0 0 3 3"><rect width="3" height="3" fill="#fff"/><g stroke="#fff" stroke-width=".08"><rect x="0" y="0" width="1" height="1" fill="#b9b9b9"/><rect x="1" y="0" width="1" height="1" fill="#cfcfcf"/><rect x="2" y="0" width="1" height="1" fill="#c4c4c4"/><rect x="0" y="1" width="1" height="1" fill="#d4d4d4"/><rect x="1" y="1" width="1" height="1" fill="#bdbdbd"/><rect x="2" y="1" width="1" height="1" fill="#d0d0d0"/><rect x="0" y="2" width="1" height="1" fill="#c2c2c2"/><rect x="1" y="2" width="1" height="1" fill="#d6d6d6"/><rect x="2" y="2" width="1" height="1" fill="#bcbcbc"/></g></svg>
  </div>
  <div class="key" style="left:232px">V3
    <svg viewBox="0 0 3 3"><g stroke="#fff" stroke-width=".08"><rect x="0" y="0" width="1" height="1" fill="#888"/><rect x="1" y="0" width="1" height="1" fill="#bbb"/><rect x="2" y="0" width="1" height="1" fill="#999"/><rect x="0" y="1" width="1" height="1" fill="#ccc"/><rect x="1" y="1" width="1" height="1" fill="#777"/><rect x="2" y="1" width="1" height="1" fill="#aaa"/><rect x="0" y="2" width="1" height="1" fill="#9a9a9a"/><rect x="1" y="2" width="1" height="1" fill="#c4c4c4"/><rect x="2" y="2" width="1" height="1" fill="#858585"/></g></svg>
  </div>
  <div class="key" style="left:263px">V4
    <svg viewBox="0 0 3 3"><g stroke="#fff" stroke-width=".08"><rect x="0" y="0" width="1" height="1" fill="#222"/><rect x="1" y="0" width="1" height="1" fill="#ddd"/><rect x="2" y="0" width="1" height="1" fill="#555"/><rect x="0" y="1" width="1" height="1" fill="#bbb"/><rect x="1" y="1" width="1" height="1" fill="#111"/><rect x="2" y="1" width="1" height="1" fill="#999"/><rect x="0" y="2" width="1" height="1" fill="#eee"/><rect x="1" y="2" width="1" height="1" fill="#444"/><rect x="2" y="2" width="1" height="1" fill="#ccc"/></g></svg>
  </div>
</section>

<!-- Styles -->
<section class="page p5">
  <div class="band">DIMENSIONS AND FEATURES</div>
  <h2 class="sec-title" style="left:0;top:69px;width:360px;text-align:center;font-size:13px">STYLES</h2>
  <p class="styles-sub">CREATE OUR OWN SIMPLE GRAPHIC FOR THESE.</p>
  <div class="style-photo" role="img" aria-label="Glass-enclosed café terrace with bistro tables on straight grain pavers" style="left:39px;top:101px;background:linear-gradient(180deg,#5d6266 0%,#3f4245 45%,#8a7f72 75%,#a6a09a 100%)"></div>
  <div class="style-name" style="left:202px;top:134px">Straight Grain</div>
  <p class="style-desc" style="left:202px;top:155px">Simple grain pattern without<br>prominent knots or features</p>
  <div class="style-name" style="left:76px;top:252px">Complex Grain</div>
  <p class="style-desc" style="left:76px;top:273px">Distinct simulated wood grain<br>with knots and details.</p>
  <div class="style-photo" role="img" aria-label="Curved rooftop walkway with railing on complex grain pavers" style="left:184px;top:219px;background:linear-gradient(180deg,#7e8c98 0%,#6a7078 40%,#8a5a44 70%,#a86e52 100%)"></div>
  <div class="style-photo" role="img" aria-label="Rooftop garden path lined with plants on weathered pavers" style="left:39px;top:335px;background:linear-gradient(180deg,#8a8f94 0%,#5f6a5a 45%,#a86c56 75%,#4c5a3c 100%)"></div>
  <div class="style-name" style="left:202px;top:368px">Weathered</div>
  <p class="style-desc" style="left:202px;top:389px">Rustic, aged look with detailed grains.</p>
</section>

</body>
</html>
```